Professional Business Cards for Recruiting Company

We'd like professional 2-sided business cards that reflect a color scheme that matches our website, www.queryvantline.com, and / or logo that is attached.

Slogan used is "We Know People", but needs to be editable because we change it up to "We Know Developers", "We Speak Geek", etc.

Must includes logo, slogan, first and last name, address, email, mobile number and website address.

Files attached for ideas.

Thanks!

Contact Information for Business Card

Logo, Company name, First name, Last name, addresss, email, phone, website address.

Font styles to use
Sans Serif

Colors
0054AA
0677BA
7BADD7
CADEEF
E8F1F8

Requirements
Nice to have
• I do like the following designs. 22962062 and 22962651. Couple ideas anyway.

```html
<!DOCTYPE html>
<html lang="en">
<head>
<meta charset="UTF-8">
<title>Queryvant Business Cards</title>
<link href="https://fonts.googleapis.com/css2?family=Montserrat:wght@400;600;700&family=Allura&display=swap" rel="stylesheet">
<style>
  :root {
    --page-bg: #d9dadc;
    --card-blue: #0d4a8f;
    --card-blue-deep: #083c7e;
    --accent-blue: #0677ba;
    --light-blue: #7badd7;
    --pale-blue: #cadeef;
    --white: #ffffff;
  }
  * { box-sizing: border-box; margin: 0; padding: 0; }
  html, body { width: 1200px; height: 800px; overflow: hidden; }
  body {
    background: var(--page-bg);
    font-family: "Montserrat", sans-serif;
    color: var(--white);
    position: relative;
  }
  .business-card {
    position: absolute;
    top: 250px;
    width: 525px;
    height: 300px;
    background: linear-gradient(135deg, var(--card-blue) 0%, var(--card-blue-deep) 100%);
    box-shadow: 0 14px 30px rgba(0,0,0,0.25);
    overflow: hidden;
  }
  .card-contact { left: 50px; }
  .card-brand { left: 625px; }

  /* contact side */
  .feature-mark {
    position: absolute;
    top: 34px;
    right: 40px;
    display: flex;
    align-items: center;
    gap: 12px;
  }
  .feature-mark .mark-dot {
    width: 24px; height: 24px;
    border-radius: 50%;
    background: var(--light-blue);
  }
  .feature-mark .mark-name {
    font-size: 30px;
    font-weight: 600;
    color: var(--light-blue);
    letter-spacing: 1px;
  }
  .contact-block {
    position: absolute;
    left: 36px;
    bottom: 30px;
  }
  .person-name {
    font-size: 21px;
    font-weight: 700;
    letter-spacing: 0.5px;
    text-transform: uppercase;
  }
  .person-title {
    font-size: 13px;
    font-weight: 400;
    color: var(--pale-blue);
    margin-bottom: 14px;
  }
  .contact-list { list-style: none; }
  .contact-list li {
    display: flex;
    align-items: center;
    gap: 9px;
    font-size: 12.5px;
    line-height: 21px;
    white-space: nowrap;
  }
  .contact-list svg { width: 12px; height: 12px; flex: none; }

  /* brand side */
  .brand-lockup {
    position: absolute;
    left: 0; right: 0;
    top: 86px;
    display: flex;
    justify-content: center;
    align-items: center;
    gap: 18px;
  }
  .brand-lockup .mark-dot {
    width: 40px; height: 40px;
    border-radius: 50%;
    background: var(--white);
  }
  .brand-lockup .brand-name {
    font-size: 46px;
    font-weight: 400;
    letter-spacing: 1px;
    line-height: 1;
    color: var(--white);
  }
  .slogan {
    position: absolute;
    left: 0; right: 0;
    top: 186px;
    text-align: center;
    font-family: "Allura", cursive;
    font-size: 54px;
    line-height: 1.2;
    color: var(--white);
  }
</style>
</head>
<body>
  <section class="business-card card-contact">
    <div class="feature-mark">
      <span class="mark-dot"></span>
      <span class="mark-name">Queryvant</span>
    </div>
    <div class="contact-block">
      <p class="person-name">Dana Kirkwell</p>
      <p class="person-title">President</p>
      <ul class="contact-list">
        <li>
          <svg viewBox="0 0 12 12"><path d="M6 0.5a4 4 0 0 0-4 4c0 3 4 7 4 7s4-4 4-7a4 4 0 0 0-4-4z" fill="#fff"/><circle cx="6" cy="4.5" r="1.5" fill="#0d4a8f"/></svg>
          Harlow Falls, North Dakota
        </li>
        <li>
          <svg viewBox="0 0 12 12"><path d="M2.5 0.8l2 2.2-1 1.4c.8 1.6 2 2.8 3.6 3.6l1.4-1 2.2 2-1.1 1.8C5 10.5 1.5 7 .8 2z" fill="#fff"/></svg>
          555-014-2287
        </li>
        <li>
          <svg viewBox="0 0 12 12"><rect x="0.5" y="2" width="11" height="8" fill="#fff"/><path d="M0.5 2l5.5 4.5L11.5 2" stroke="#0d4a8f" fill="none"/></svg>
          dana.kirkwell@queryvantline.com
        </li>
        <li>
          <svg viewBox="0 0 12 12"><circle cx="6" cy="6" r="5.2" fill="none" stroke="#fff" stroke-width="1.2"/><path d="M0.8 6h10.4M6 0.8c-2.5 2.8-2.5 7.6 0 10.4M6 0.8c2.5 2.8 2.5 7.6 0 10.4" stroke="#fff" fill="none" stroke-width="0.9"/></svg>
          www.queryvantline.com
        </li>
      </ul>
    </div>
  </section>

  <section class="business-card card-brand">
    <div class="brand-lockup">
      <span class="mark-dot"></span>
      <p class="brand-name">Queryvant</p>
    </div>
    <p class="slogan">We Know People</p>
  </section>
</body>
</html>
```